Web Design for Financial Consulting Company

We need a website design for a financial consulting company "Kelvane Consulting". We build financial models, scenario analysis, handle the budgeting process and provide temporary staffing. I have over 10 years of experience. My Excel expertise and analytical savvy has saved clients over $17 million in profit.

Target Market(s)

Small to medium businesses

Industry/Entity Type

Financial Consulting

Number of Pages Required

4 page

Requirements
Must have
• Professional looking
Nice to have
• A little futuristic looking

```html
<!DOCTYPE html>
<html lang="en">
<head>
<meta charset="UTF-8">
<title>Kelvane Consulting</title>
<link href="https://fonts.googleapis.com/css2?family=Poppins:wght@400;500;600;700&display=swap" rel="stylesheet">
<style>
:root{
  --blue:#00a8ec;
  --navy:#0a3a63;
  --deep:#0b4f86;
  --ink:#1f1f1f;
  --muted:#6a6f76;
  --pale:#f2f9fd;
  --line:#d9dde2;
  --dark:#2a2a2a;
  --star:#f6b70b;
}
*{margin:0;padding:0;box-sizing:border-box}
html,body{width:1200px;height:2941px;overflow:hidden}
body{font-family:'Poppins',sans-serif;color:var(--ink);position:relative;background:#fff}
.abs{position:absolute}
a{color:inherit;text-decoration:none}

/* top bar */
.topbar{position:absolute;left:0;top:0;width:1200px;height:56px;background:#fff}
.brand{display:flex;align-items:center;gap:8px;font-weight:600;font-size:20px;color:var(--navy);letter-spacing:.3px}
.brand .mark{width:24px;height:24px;border:2.5px solid var(--blue)}
.topbar .brand{position:absolute;left:112px;top:15px}
.contact-item{position:absolute;top:11px;display:flex;gap:12px;align-items:center}
.contact-item .ico{width:35px;height:35px;border:1px solid var(--line);display:flex;align-items:center;justify-content:center}
.contact-item small{display:block;font-size:10px;color:var(--muted)}
.contact-item b{font-size:11px;font-weight:600}
.socials{position:absolute;top:11px;left:914px;display:flex;gap:11px}
.socials span{width:35px;height:35px;border:1px solid var(--line);display:block}

/* nav */
.nav{position:absolute;left:0;top:56px;width:1200px;height:50px;background:var(--blue);color:#fff;font-size:12px}
.nav ul{list-style:none;display:flex;gap:36px;position:absolute;left:112px;top:18px}
.nav li.active{font-weight:700}
.search{position:absolute;left:681px;top:18px;width:172px;border-bottom:1px solid rgba(255,255,255,.6);padding-bottom:6px;font-size:12px}
.search svg{position:absolute;left:172px;top:-4px}
.cta-dark{position:absolute;left:916px;top:4px;width:171px;height:42px;background:var(--navy);border-radius:4px;display:flex;align-items:center;justify-content:center;font-weight:600;font-size:13px}

/* hero */
.hero{position:absolute;left:0;top:106px;width:1200px;height:509px;background:linear-gradient(100deg,#0b4a80 0%,#0c5d97 40%,#1f7db3 65%,#0c3f6a 100%)}
.hero h1{position:absolute;left:112px;top:99px;width:600px;font-size:50px;line-height:56px;font-weight:700;color:#fff}
.hero p{position:absolute;left:112px;top:286px;width:440px;font-size:15.5px;line-height:22px;color:#eaf5ff}
.stat{position:absolute;top:577px;height:78px;background:#fff;border-radius:4px;box-shadow:0 10px 30px rgba(0,40,80,.12);display:flex;align-items:center;gap:16px;padding-left:44px;font-weight:600;font-size:14px;overflow:hidden}
.stat .bars{position:absolute;right:30px;bottom:0}

/* about */
.about-photo{position:absolute;left:113px;top:717px;width:347px;height:378px;border-radius:6px;background:linear-gradient(135deg,#2d4f7a,#6a8fb5 45%,#b48a60 75%,#3a3a3a)}
.play{position:absolute;left:412px;top:965px;width:94px;height:94px;border-radius:50%;background:#fff;box-shadow:0 0 0 14px rgba(255,255,255,.35)}
.eyebrow{font-size:13px;font-weight:600;color:var(--blue)}
.h2{font-size:33px;line-height:38px;font-weight:600;color:var(--ink)}
.about .eyebrow{position:absolute;left:591px;top:725px}
.about .h2{position:absolute;left:589px;top:754px}
.about p{position:absolute;left:591px;top:844px;width:485px;font-size:11.5px;line-height:19px;color:var(--muted)}
.ticks{list-style:none;font-size:13px;color:#333}
.ticks li{position:relative;padding-left:28px;height:33px}
.ticks li::before{content:"";position:absolute;left:0;top:4px;width:14px;height:14px;border-radius:50%;background:var(--navy)}
.about .ticks{position:absolute;left:591px;top:934px}
.btn{display:flex;align-items:center;justify-content:center;background:var(--blue);color:#fff;font-weight:600;font-size:13px;border-radius:4px}
.about .btn{position:absolute;left:591px;top:1039px;width:172px;height:50px}

/* services */
.services{position:absolute;left:0;top:1170px;width:1200px;height:542px;background:var(--pale)}
.services .eyebrow{position:absolute;left:112px;top:62px}
.services .h2{position:absolute;left:112px;top:88px}
.services .btn{position:absolute;left:916px;top:102px;width:171px;height:49px}
.card{position:absolute;top:208px;width:232px;height:271px;background:#fff;border-radius:6px;box-shadow:0 4px 18px rgba(0,60,100,.06);text-align:center}
.card .circle{width:84px;height:84px;border-radius:50%;margin:36px auto 0;box-shadow:0 6px 18px rgba(0,80,140,.12);display:flex;align-items:center;justify-content:center}
.card h3{font-size:16px;font-weight:600;margin-top:20px}
.card p{font-size:11.5px;line-height:19px;color:var(--muted);margin:10px 18px 0}

/* testimonial */
.testi{position:absolute;left:0;top:1712px;width:1200px;height:518px;background:linear-gradient(120deg,#0aa6ea 0%,#0a8fd4 50%,#0a6eb4 100%)}
.testi .eyebrow{position:absolute;width:100%;top:54px;text-align:center;color:var(--navy)}
.testi h2{position:absolute;width:100%;top:83px;text-align:center;color:#fff;font-size:30px;font-weight:600}
.tcard{position:absolute;top:158px;width:442px;height:248px;background:#fff;border-radius:6px}
.avatar{position:absolute;left:39px;top:28px;width:84px;height:84px;border-radius:50%;border:2px solid var(--navy);background:radial-gradient(circle at 50% 40%,#c9a58a,#5b6f86)}
.tcard h4{position:absolute;left:145px;top:38px;font-size:16px;font-weight:600}
.tcard .role{position:absolute;left:145px;top:64px;font-size:13px;color:var(--blue)}
.tcard .stars{position:absolute;left:145px;top:86px}
.tcard .quote{position:absolute;right:46px;top:6px;font-size:120px;line-height:120px;color:#cfd2d6;font-weight:700}
.tcard p{position:absolute;left:53px;top:128px;width:346px;font-size:12.5px;line-height:19px;color:var(--muted)}
.dots{position:absolute;top:2156px;left:571px;display:flex;gap:13px}
.dots span{width:10px;height:10px;border-radius:50%;background:rgba(255,255,255,.5)}
.dots span:first-child{background:#fff}

/* contact */
.contact .eyebrow{position:absolute;left:112px;top:2287px}
.contact .h2{position:absolute;left:112px;top:2314px}
.contact p{position:absolute;left:112px;top:2404px;width:500px;font-size:13px;line-height:19px;color:var(--muted)}
.contact .ticks{position:absolute;left:112px;top:2485px}
.support{position:absolute;left:112px;top:2599px;display:flex;gap:22px;align-items:center}
.support .ph{width:50px;height:50px;border-radius:50%;background:var(--blue);display:flex;align-items:center;justify-content:center}
.support small{display:block;font-size:13px;font-weight:600}
.support b{font-size:17px;font-weight:600;color:var(--blue);letter-spacing:.5px}
.quote-form{position:absolute;left:694px;top:2280px;width:393px;height:374px;background:#fff;border-radius:6px;box-shadow:0 6px 30px rgba(0,40,80,.08)}
.quote-form .eyebrow{position:absolute;left:29px;top:41px}
.quote-form h2{position:absolute;left:28px;top:65px;font-size:32px;font-weight:600}
.field{position:absolute;width:161px;height:40px;border:1px solid var(--line);border-radius:3px;font-size:10.5px;color:#999;padding:13px 18px}
.field.sel::after{content:"";position:absolute;right:14px;top:14px;width:6px;height:6px;border-right:1px solid #888;border-bottom:1px solid #888;transform:rotate(45deg)}
.quote-form .btn{position:absolute;left:30px;top:282px;width:172px;height:50px}

/* footer */
.footer{position:absolute;left:0;top:2717px;width:1200px;height:224px;background:var(--dark);color:#fff}
.footer .brand{position:absolute;left:489px;top:30px;color:#fff;font-size:24px}
.footer .rule{position:absolute;top:110px;height:1px;background:#555;width:380px}
.fsoc{position:absolute;left:514px;top:92px;display:flex;gap:13px}
.fsoc span{width:33px;height:33px;background:var(--navy);display:block}
.footer ul{list-style:none;display:flex;gap:36px;position:absolute;left:470px;top:144px;font-size:12px}
.footer .copy{position:absolute;width:100%;top:190px;text-align:center;font-size:11px}
</style>
</head>
<body>

<header class="topbar">
  <div class="brand"><span class="mark"></span>Kelvane Consulting</div>
  <div class="contact-item" style="left:365px">
    <span class="ico"><svg width="14" height="18" viewBox="0 0 14 18"><path d="M7 1a6 6 0 0 0-6 6c0 4.5 6 10 6 10s6-5.5 6-10a6 6 0 0 0-6-6z" fill="none" stroke="#00a8ec" stroke-width="2"/><circle cx="7" cy="7" r="2" fill="#00a8ec"/></svg></span>
    <div><small>Email Us:</small><b>hello@kelvaneconsulting.com</b></div>
  </div>
  <div class="contact-item" style="left:659px">
    <span class="ico"><svg width="16" height="16" viewBox="0 0 24 24"><path d="M6.6 10.8a15 15 0 0 0 6.6 6.6l2.2-2.2a1 1 0 0 1 1-.25 11.4 11.4 0 0 0 3.6.6 1 1 0 0 1 1 1V20a1 1 0 0 1-1 1A17 17 0 0 1 3 4a1 1 0 0 1 1-1h3.5a1 1 0 0 1 1 1c0 1.25.2 2.45.6 3.6a1 1 0 0 1-.25 1z" fill="#00a8ec"/></svg></span>
    <div><small>Get Call Us:</small><b>(+044) 310 778 512</b></div>
  </div>
  <div class="socials" aria-label="Social links"><span></span><span></span><span></span><span></span></div>
</header>

<nav class="nav">
  <ul><li class="active">Home</li><li>About</li><li>Service</li><li>Contact</li></ul>
  <div class="search">Search
    <svg width="20" height="20" viewBox="0 0 20 20"><circle cx="8" cy="8" r="6" fill="none" stroke="#fff" stroke-width="2"/><line x1="12.5" y1="12.5" x2="18" y2="18" stroke="#fff" stroke-width="2"/></svg>
  </div>
  <div class="cta-dark">Request &amp; Call</div>
</nav>

<section class="hero" role="img" aria-label="Businessman drawing a rising growth chart over digital finance graphics">
  <h1>Helping your finance team and increasing profit</h1>
  <p>Lorem ipsum dolor sit amet, consectetur adipiscing elit, sed do eiusmod tempor incididunt ut labore et dolore magna aliqua.</p>
</section>

<div class="stat" style="left:176px;width:414px">
  <svg width="36" height="42" viewBox="0 0 36 42"><circle cx="18" cy="14" r="12" fill="#00a8ec"/><rect x="8" y="24" width="16" height="16" rx="3" fill="#00a8ec"/></svg>
  Over 10 years of experience
  <svg class="bars" width="70" height="70" viewBox="0 0 70 70"><g fill="#e3f4fc"><rect x="4" y="46" width="12" height="24"/><rect x="22" y="32" width="12" height="38"/><rect x="40" y="18" width="12" height="52"/><rect x="58" y="4" width="12" height="66"/></g></svg>
</div>
<div class="stat" style="left:610px;width:414px">
  <svg width="40" height="40" viewBox="0 0 40 40"><circle cx="22" cy="12" r="10" fill="#00a8ec"/><text x="22" y="17" font-size="13" fill="#fff" text-anchor="middle" font-family="Poppins,sans-serif" font-weight="700">$</text><path d="M2 26h8v12H2zM12 28h10c4 0 6 2 12-2l2 2c-6 6-10 8-16 8h-8z" fill="#0a3a63"/></svg>
  <span>I have successfully increased<br>profitability for clients by $17M.</span>
  <svg class="bars" width="70" height="70" viewBox="0 0 70 70"><g fill="#e3f4fc"><rect x="4" y="46" width="12" height="24"/><rect x="22" y="32" width="12" height="38"/><rect x="40" y="18" width="12" height="52"/><rect x="58" y="4" width="12" height="66"/></g></svg>
</div>

<section class="about">
  <div class="about-photo" role="img" aria-label="Team of consultants reviewing work on a laptop"></div>
  <div class="play"><svg width="94" height="94" viewBox="0 0 94 94"><path d="M37 31l26 16-26 16z" fill="#00a8ec"/></svg></div>
  <div class="eyebrow">About Our Company</div>
  <h2 class="h2">Read The Story Behind<br>Our Success</h2>
  <p>I am an experienced Finance professional who develops strategic financial plans, provides insightful analysis, and supports decision-making. With over 10 years of experience, I have successfully increased profitability<br>for clients by $17M.</p>
  <ul class="ticks">
    <li>Premium services and beyond your expectation</li>
    <li>Get the best support among all venders</li>
    <li>Fully responsive and works great on all major devices</li>
  </ul>
  <a class="btn">More About Us</a>
</section>

<section class="services">
  <div class="eyebrow">Our Service</div>
  <h2 class="h2">We run all kinds of service<br>that your success</h2>
  <a class="btn">View More</a>
  <div class="card" style="left:113px">
    <div class="circle"><svg width="40" height="40" viewBox="0 0 40 40"><g stroke="#00a8ec" stroke-width="3"><line x1="8" y1="8" x2="32" y2="32"/><line x1="32" y1="8" x2="8" y2="32"/></g><g fill="#00a8ec"><circle cx="6" cy="6" r="5"/><circle cx="34" cy="6" r="5"/><circle cx="6" cy="34" r="5"/><circle cx="34" cy="34" r="5"/><circle cx="20" cy="20" r="10"/></g><text x="20" y="25" font-size="13" fill="#fff" text-anchor="middle" font-family="Poppins,sans-serif" font-weight="700">$</text></svg></div>
    <h3>Financial Models</h3>
    <p>Financial analysis, scenario modeling, pricing analysis, projects</p>
  </div>
  <div class="card" style="left:360px">
    <div class="circle"><svg width="42" height="42" viewBox="0 0 42 42"><circle cx="21" cy="21" r="17" fill="none" stroke="#00a8ec" stroke-width="3" stroke-dasharray="22 5"/><circle cx="21" cy="15" r="8" fill="#00a8ec"/><text x="21" y="19.5" font-size="11" fill="#fff" text-anchor="middle" font-family="Poppins,sans-serif" font-weight="700">$</text><circle cx="21" cy="30" r="6" fill="none" stroke="#0a3a63" stroke-width="2.5"/></svg></div>
    <h3>Budgeting Process</h3>
    <p>Building budgets from scratch, revamping current process to be more robust and scalable.</p>
  </div>
  <div class="card" style="left:607px">
    <div class="circle"><svg width="40" height="30" viewBox="0 0 40 30"><g fill="#00a8ec"><circle cx="20" cy="7" r="6"/><circle cx="8" cy="10" r="4.5"/><circle cx="32" cy="10" r="4.5"/><rect x="12" y="15" width="16" height="14" rx="4"/><rect x="1" y="17" width="11" height="12" rx="3"/><rect x="28" y="17" width="11" height="12" rx="3"/></g></svg></div>
    <h3>Temporary Staffing</h3>
    <p>Years of Financial Planning and Analysis experience across multiple industries can help temporary staffing needs.</p>
  </div>
  <div class="card" style="left:854px">
    <div class="circle"><svg width="42" height="42" viewBox="0 0 42 42"><circle cx="21" cy="21" r="15" fill="none" stroke="#00a8ec" stroke-width="7" stroke-dasharray="6 4"/><circle cx="21" cy="21" r="11" fill="#00a8ec"/><path d="M21 13l7 8h-4v7h-6v-7h-4z" fill="#fff"/></svg></div>
    <h3>Process Improvement</h3>
    <p>Month end close, reporting, budg</p>
  </div>
</section>

<section class="testi">
  <div class="eyebrow">Testimonial</div>
  <h2>What Happy Clients Say?</h2>
  <div class="tcard" style="left:148px">
    <div class="avatar" role="img" aria-label="Portrait of client"></div>
    <h4>Owen Farraday</h4>
    <div class="role">Co- Of Officer</div>
    <svg class="stars" width="112" height="18" viewBox="0 0 112 18"><defs><path id="st" d="M8 0l2.4 5.3 5.6.6-4.2 3.8 1.2 5.6L8 12.4 3 15.3l1.2-5.6L0 5.9l5.6-.6z"/></defs><g fill="#f6b70b"><use href="#st"/><use href="#st" x="23"/><use href="#st" x="46"/><use href="#st" x="69"/><use href="#st" x="92"/></g></svg>
    <div class="quote">”</div>
    <p>Lorem ipsum dolor sit amet, consectetur adipiscing elit, sed do eiusmod tempor incididunt ut labore et dolore magna aliqua. Quis ipsum suspendisse ultrices gravida. Risus commodo viverra maecenas accumsan lacus vel facilisis.</p>
  </div>
  <div class="tcard" style="left:610px">
    <div class="avatar" role="img" aria-label="Portrait of client"></div>
    <h4>Rina Castell</h4>
    <div class="role">Manager</div>
    <svg class="stars" width="112" height="18" viewBox="0 0 112 18"><g fill="#f6b70b"><use href="#st"/><use href="#st" x="23"/><use href="#st" x="46"/><use href="#st" x="69"/><use href="#st" x="92"/></g></svg>
    <div class="quote">”</div>
    <p>Lorem ipsum dolor sit amet, consectetur adipiscing elit, sed do eiusmod tempor incididunt ut labore et dolore magna aliqua. Quis ipsum suspendisse ultrices gravida. Risus commodo viverra maecenas accumsan lacus vel facilisis.</p>
  </div>
</section>
<div class="dots"><span></span><span></span><span></span></div>

<section class="contact">
  <div class="eyebrow">Get In Touch</div>
  <h2 class="h2">What We Can Help<br>For You</h2>
  <p>Lorem ipsum dolor sit amet, consectetur adipiscing elit. Curabitur commodo eleifend hendrerit. Vivamus sodales, sem et accumsan fermentum, erat enim dignissim risus, et convallis erat nisl ut mauris.</p>
  <ul class="ticks">
    <li>27 Harbour Lane, Westmere</li>
    <li>Which don't Look Even Slightly Believable</li>
    <li>402 517 3381 640</li>
  </ul>
  <div class="support">
    <span class="ph"><svg width="20" height="20" viewBox="0 0 24 24"><path d="M6.6 10.8a15 15 0 0 0 6.6 6.6l2.2-2.2a1 1 0 0 1 1-.25 11.4 11.4 0 0 0 3.6.6 1 1 0 0 1 1 1V20a1 1 0 0 1-1 1A17 17 0 0 1 3 4a1 1 0 0 1 1-1h3.5a1 1 0 0 1 1 1c0 1.25.2 2.45.6 3.6a1 1 0 0 1-.25 1z" fill="#fff"/></svg></span>
    <div><small>Quick Support Number</small><b>(+44 3120 7745 18)</b></div>
  </div>
  <form class="quote-form">
    <div class="eyebrow">Contact Us</div>
    <h2>Request A Quote</h2>
    <div class="field" style="left:29px;top:118px">Name</div>
    <div class="field" style="left:202px;top:118px">Eamil</div>
    <div class="field sel" style="left:29px;top:170px">Select Company</div>
    <div class="field sel" style="left:202px;top:170px">Select Staircase</div>
    <div class="field" style="left:29px;top:221px">Phone</div>
    <div class="field sel" style="left:202px;top:221px">Room Select</div>
    <a class="btn">Send Message</a>
  </form>
</section>

<footer class="footer">
  <div class="brand"><span class="mark"></span>Kelvane Consulting</div>
  <div class="rule" style="left:118px"></div>
  <div class="rule" style="left:704px"></div>
  <div class="fsoc" aria-label="Social links"><span></span><span></span><span></span><span></span></div>
  <ul><li style="font-weight:700">Home</li><li>About</li><li>Service</li><li>Contact</li></ul>
  <div class="copy">Copyright © 2010-2023 All rights reserved.</div>
</footer>

</body>
</html>
```